KORBALT

The business want a professional looking business card. We have a scetch we will add but want the extra upgrade, and would like more suggestions for variations of our business cards.

```html
<!DOCTYPE html>
<html lang="en">
<head>
<meta charset="utf-8">
<title>KORBALT Business Card</title>
<link href="https://fonts.googleapis.com/css2?family=Marcellus&family=Sora:wght@400&family=Josefin+Sans:wght@300&display=swap" rel="stylesheet">
<style>
  :root {
    --page: #f4f4f2;
    --card: #000000;
    --gold: #c39a2b;
    --shadow: rgba(0, 0, 0, 0.28);
  }
  html, body {
    margin: 0;
    padding: 0;
    width: 1200px;
    height: 1200px;
    overflow: hidden;
    background: var(--page);
  }
  .canvas {
    position: relative;
    width: 1200px;
    height: 1200px;
  }
  .card {
    position: absolute;
    left: 290px;
    width: 620px;
    height: 354px;
    background: var(--card);
    border-radius: 10px;
    box-shadow: 4px 6px 10px var(--shadow);
    color: var(--gold);
  }
  .card--front { top: 222px; }
  .card--back { top: 623px; }

  .brand {
    position: absolute;
    display: flex;
    flex-direction: column;
    align-items: center;
    transform: translateX(-50%);
  }
  .brand__dot {
    border-radius: 50%;
    background: var(--gold);
  }
  .brand__name {
    font-family: "Marcellus", serif;
    color: var(--gold);
    letter-spacing: 0.28em;
    margin-right: -0.28em;
    line-height: 1;
  }
  .card--front .brand { left: 310px; top: 110px; }
  .card--front .brand__dot { width: 64px; height: 64px; margin-bottom: 34px; }
  .card--front .brand__name { font-size: 29px; }

  .card--back .brand { left: 512px; top: 42px; }
  .card--back .brand__dot { width: 52px; height: 52px; margin-bottom: 28px; }
  .card--back .brand__name { font-size: 22px; }

  .person {
    position: absolute;
    left: 41px;
    top: 156px;
  }
  .person__name {
    font-family: "Marcellus", serif;
    font-size: 24px;
    line-height: 1;
    margin: 0;
    letter-spacing: 0.01em;
    -webkit-text-stroke: 0.6px var(--gold);
  }
  .person__role {
    font-family: "Josefin Sans", sans-serif;
    font-weight: 300;
    font-size: 19px;
    letter-spacing: 0.14em;
    margin: 6px 0 0;
    line-height: 1;
  }
  .person__owner {
    font-family: "Marcellus", serif;
    font-size: 14px;
    margin: 8px 0 0;
    line-height: 1;
    -webkit-text-stroke: 0.3px var(--gold);
  }

  .divider {
    position: absolute;
    left: 43px;
    top: 246px;
  }

  .contact {
    position: absolute;
    display: flex;
    align-items: center;
    font-family: "Sora", sans-serif;
    font-size: 17px;
    line-height: 1;
  }
  .contact svg { flex: none; margin-right: 12px; }
  .contact--location { left: 45px; top: 289px; }
  .contact--phone { left: 45px; top: 314px; }
  .contact--email { left: 324px; top: 289px; }
  .contact--web { left: 324px; top: 314px; }
</style>
</head>
<body>
<div class="canvas">

  <section class="card card--front">
    <div class="brand">
      <div class="brand__dot"></div>
      <div class="brand__name">KORBALT</div>
    </div>
  </section>

  <section class="card card--back">
    <div class="brand">
      <div class="brand__dot"></div>
      <div class="brand__name">KORBALT</div>
    </div>

    <div class="person">
      <h1 class="person__name">KORBALT VOLDHAUG</h1>
      <p class="person__role">CEO &amp; Founder</p>
      <p class="person__owner">ANDERS MIKAEL VOLDHAUG</p>
    </div>

    <svg class="divider" width="536" height="8" viewBox="0 0 536 8" aria-hidden="true">
      <rect x="0" y="2.5" width="536" height="3" fill="#c39a2b"/>
      <rect x="145" y="0" width="245" height="8" rx="4" fill="#c39a2b"/>
    </svg>

    <div class="contact contact--location">
      <svg width="16" height="16" viewBox="0 0 16 16" aria-label="Address">
        <circle cx="8" cy="8" r="8" fill="#c39a2b"/>
        <path d="M8 3.5a3 3 0 0 0-3 3c0 2.2 3 5.5 3 5.5s3-3.3 3-5.5a3 3 0 0 0-3-3z" fill="#000"/>
        <circle cx="8" cy="6.5" r="1.1" fill="#c39a2b"/>
      </svg>
    </div>

    <div class="contact contact--phone">
      <svg width="16" height="16" viewBox="0 0 16 16" aria-label="Phone">
        <circle cx="8" cy="8" r="8" fill="#c39a2b"/>
        <path d="M4 7.2c0-1.4 1.8-2.2 4-2.2s4 .8 4 2.2v.6h-2v-1H6v1H4z M5 8.5h6l.6 2.7H4.4z" fill="#000"/>
      </svg>
      <span>004791234567</span>
    </div>

    <div class="contact contact--email">
      <svg width="16" height="16" viewBox="0 0 16 16" aria-label="Email">
        <circle cx="8" cy="8" r="8" fill="#c39a2b"/>
        <rect x="4" y="5.3" width="8" height="5.4" rx="0.6" fill="#000"/>
        <path d="M4.4 5.8 8 8.6l3.6-2.8" stroke="#c39a2b" stroke-width="0.8" fill="none"/>
      </svg>
      <span>korbalt.llc@outlock.com</span>
    </div>

    <div class="contact contact--web">
      <svg width="16" height="16" viewBox="0 0 16 16" aria-label="Website">
        <circle cx="8" cy="8" r="8" fill="#c39a2b"/>
        <g stroke="#000" stroke-width="0.8" fill="none">
          <circle cx="8" cy="8" r="3.8"/>
          <ellipse cx="8" cy="8" rx="1.6" ry="3.8"/>
          <path d="M4.2 8h7.6M4.8 6h6.4M4.8 10h6.4"/>
        </g>
      </svg>
      <span>www.korbalt.llc</span>
    </div>
  </section>

</div>
</body>
</html>
```